Modern Lawfirm Business Card Design

We're looking for a business card to incorporate the newly created logo we had made.

Ideally looking for a law firm business card demonstrating, modern, minimalist, strong/bold design.

I'm open to any design honestly, but nothing "flashy".

Target Market(s)

Immigration law, family immigration, humanitarian, general legal

Industry/Entity Type

Law Firm

Contact Information for Business Card

Please use dummy information, name, street address, city, state, phone number, email, website.

Font styles to use
Serif
Sans Serif

Requirements
Must have
• Please use dummy information, name, street address, city, state, phone number, email, website.

```html
<!DOCTYPE html>
<html lang="en">
<head>
<meta charset="utf-8">
<title>Valtierra Immigration Law — Business Card</title>
<link rel="stylesheet" href="https://fonts.googleapis.com/css2?family=Roboto:wght@400;500;700&family=Roboto+Condensed:wght@700&display=swap">
<style>
  :root {
    --bg: #e6e6e6;
    --navy: #24385e;
    --navy-deep: #1f3154;
    --gold: #c2a461;
    --ink-light: #eef0f5;
  }
  * { box-sizing: border-box; margin: 0; padding: 0; }
  html, body { width: 1200px; height: 900px; overflow: hidden; }
  body {
    background: var(--bg);
    font-family: "Roboto", sans-serif;
    position: relative;
  }
  .card {
    position: absolute;
    width: 600px;
    height: 343px;
    background: radial-gradient(ellipse at 45% 45%, var(--navy) 0%, var(--navy-deep) 100%);
    box-shadow: 0 6px 18px rgba(0,0,0,0.18);
  }
  .card--front { left: 180px; top: 70px; }
  .card--back { left: 420px; top: 470px; }

  .wordmark {
    display: flex;
    align-items: center;
    gap: 10px;
    color: var(--gold);
    font-family: "Roboto", sans-serif;
    font-weight: 500;
    text-transform: uppercase;
    white-space: nowrap;
  }
  .wordmark__square { background: var(--gold); flex: none; }

  .card--front .wordmark {
    position: absolute;
    left: 50%; top: 50%;
    transform: translate(-50%, -50%);
    font-size: 26px;
    letter-spacing: 3px;
  }
  .card--front .wordmark__square { width: 16px; height: 16px; }

  .card--back .wordmark {
    position: absolute;
    right: 34px; top: 34px;
    font-size: 15px;
    letter-spacing: 2px;
  }
  .card--back .wordmark__square { width: 10px; height: 10px; }

  .contact {
    position: absolute;
    left: 40px; bottom: 34px;
    color: var(--ink-light);
  }
  .contact__name {
    font-family: "Roboto Condensed", sans-serif;
    font-weight: 700;
    font-size: 26px;
    color: var(--gold);
    letter-spacing: 0.5px;
    line-height: 1;
  }
  .contact__role {
    font-size: 11px;
    font-weight: 500;
    letter-spacing: 1px;
    text-transform: uppercase;
    margin: 4px 0 12px;
  }
  .contact__list { list-style: none; }
  .contact__item {
    display: flex;
    align-items: center;
    gap: 10px;
    font-size: 12px;
    letter-spacing: 0.8px;
    line-height: 19px;
  }
  .contact__icon { width: 12px; height: 12px; flex: none; fill: none; stroke: var(--gold); stroke-width: 1.6; }
  .contact__icon--solid { fill: var(--gold); stroke: none; }
  .contact__address {
    font-size: 12px;
    letter-spacing: 0.8px;
    line-height: 16px;
    margin-top: 8px;
  }
  .contact__web {
    font-size: 12px;
    font-weight: 700;
    letter-spacing: 1.4px;
    color: var(--gold);
    margin-top: 8px;
  }
</style>
</head>
<body>

  <section class="card card--front" aria-label="Card front">
    <div class="wordmark">
      <span class="wordmark__square"></span>
      <span>Valtierra Immigration Law</span>
    </div>
  </section>

  <section class="card card--back" aria-label="Card back">
    <div class="wordmark">
      <span class="wordmark__square"></span>
      <span>Valtierra Immigration Law</span>
    </div>

    <div class="contact">
      <h1 class="contact__name">JOHN DOE</h1>
      <p class="contact__role">Director</p>
      <ul class="contact__list">
        <li class="contact__item">
          <svg class="contact__icon" viewBox="0 0 12 12"><rect x="2.5" y="0.8" width="7" height="10.4" rx="1"/></svg>
          123 456 7890
        </li>
        <li class="contact__item">
          <svg class="contact__icon contact__icon--solid" viewBox="0 0 12 12"><path d="M2 1h2.5l1 3-1.5 1a6 6 0 0 0 3 3l1-1.5 3 1V11h-1.5A9 9 0 0 1 1 2.5V1z"/></svg>
          123 456 7890
        </li>
        <li class="contact__item">
          <svg class="contact__icon contact__icon--solid" viewBox="0 0 12 12"><rect x="3" y="1" width="6" height="3"/><rect x="1" y="5" width="10" height="6" rx="1"/></svg>
          +12 484 2907
        </li>
        <li class="contact__item">
          <svg class="contact__icon" viewBox="0 0 12 12"><rect x="1" y="2.5" width="10" height="7"/><path d="M1 2.5l5 4 5-4"/></svg>
          john@valtierraimmigration.com
        </li>
      </ul>
      <p class="contact__address">Harbor Point Complex<br>Meridian, Indonesia</p>
      <p class="contact__web">www.valtierraimmigration.com</p>
    </div>
  </section>

</body>
</html>
```